One-page Capabilities Statement needed

Seeking a one-page, visually appealing capabilities statement also known as a marketing one-page slick. I have attached a word document that contains all the content required to populate the capabilities statement. Please feel free to use the attached example PDF as a starting point and I will provide comments as design concepts are received.
Updates

Project was launched today; I am not sure why it states a due date of 11/6/2018.

Target Market(s)

Federal Agencies

Industry/Entity Type

Consulting

Requirements
Must have
• Must contain the same color scheme as the attached example (see pdf document). Document can not exceed 2MB in file size - please compress as much as possible.

```html
<!DOCTYPE html>
<html lang="en">
<head>
<meta charset="utf-8">
<title>Capability Statement</title>
<link href="https://fonts.googleapis.com/css2?family=Raleway:wght@600;700;800&family=Open+Sans:ital,wght@0,400;0,600;1,400&display=swap" rel="stylesheet">
<style>
:root{
  --navy:#1d3768;
  --blue:#2e6fb7;
  --sky:#4a8fd4;
  --ink:#5a5f66;
  --paper:#ffffff;
}
*{box-sizing:border-box;margin:0;padding:0}
html,body{width:769px;height:1200px;overflow:hidden;background:var(--paper)}
body{font-family:"Open Sans",Arial,sans-serif;color:var(--ink);font-size:11px;line-height:1.55;position:relative}
.masthead{position:absolute;left:0;top:0;width:769px;height:48px;background:var(--navy);display:flex;align-items:center;padding-left:22px}
.masthead h1{font-family:"Raleway",Arial,sans-serif;font-weight:800;color:#fff;font-size:28px;letter-spacing:.2px}
.column{position:absolute;top:58px}
.column.left{left:22px;width:352px}
.column.right{left:400px;width:350px}
.section-title{font-family:"Raleway",Arial,sans-serif;color:var(--blue);font-weight:700;font-size:18px;line-height:1.3;margin:0 0 6px}
.section-label{font-family:"Raleway",Arial,sans-serif;color:var(--navy);font-weight:800;font-size:14.5px;line-height:1.3;margin:0 0 5px}
p{margin:0 0 14px}
.right p{font-style:italic}
.ring-list{list-style:none;margin:0 0 14px}
.ring-list li{position:relative;padding-left:26px;margin-bottom:10px;font-style:italic}
.ring-list li::before{content:"";position:absolute;left:2px;top:2px;width:13px;height:13px;border:2px solid var(--sky);border-radius:50%}
.data-grid{display:grid;grid-template-columns:118px 1fr;column-gap:10px;font-style:italic;margin-bottom:16px}
.footer{position:absolute;left:0;bottom:0;width:769px;height:78px;background:var(--navy);padding:12px 22px;color:#fff}
.footer h3{font-family:"Raleway",Arial,sans-serif;font-weight:700;font-size:14px;letter-spacing:.6px;color:#fff;margin-bottom:4px}
.footer .line{font-size:9.6px;line-height:1.4}
.footer .name{font-weight:600}
</style>
</head>
<body>
<header class="masthead"><h1>Capability Statement</h1></header>

<section class="column left">
  <h2 class="section-title">THE TEAM</h2>
  <h3 class="section-label">Corporate Leadership</h3>
  <p>Daniel Marsh, president, brings more than 25 years of experience in environmental policy and planning as well as federal and tribal relations. He has served in senior leadership roles within federal energy policy programs, led a national tribal environmental organization, directed environmental programs for a multi-tribe resource council, and worked as a policy analyst on environmental restoration and waste management. Daniel holds a graduate degree in Environmental Science and Policy.</p>

  <h3 class="section-label">Technical Team</h3>
  <p>Cedar Ridge Environmental Services has built a technical team uniting some of the foremost NEPA experts in the country who bring decades of experience working with and on behalf of numerous federal agencies, including the office that oversees the implementation of NEPA across all federal agencies. The technical team encompasses industry experts, former government personnel, scientists, planners, and attorneys with advanced expertise in developing NEPA regulations, policies, compliance strategies, and analyses at the highest levels of government.</p>

  <h3 class="section-label">Senior Advisor</h3>
  <p>Roy Hale, senior advisor, is a subject matter expert with a long career in federal installations and environmental management, where he was responsible for facilities worldwide and acted as steward of millions of acres of public land. This encompassed military construction, family housing, and all real estate transactions along with all environmental and natural resource management programs.</p>

  <h2 class="section-title">Technical Capabilities</h2>
  <ul class="ring-list">
    <li>Preparation of Categorical Exclusions, Environmental Assessments/Findings of No Significant Impact, and Environmental Impact Statements.</li>
    <li>Determination of NEPA Adequacy documents.</li>
    <li>Stewardship of Environmental Permitting (NEPA, ESA, NHPA, CWA) and regulatory compliance, Environmental Justice Advisory Services, etc.</li>
    <li>Contributions to Tribal Consultation and Cultural Resource Assessment.</li>
  </ul>

  <h2 class="section-title">Partnership</h2>
  <p>Beyond in-house technical capacities, CRES has partnered with Brightwater Consulting Services (BCS) to consistently ensure exceptional service delivery.</p>
</section>

<section class="column right">
  <p>BCS further provides diverse technical and community relations expertise, federal contract management, accurate, clearly written technical documents, and a proven organizational structure with a strong communication network. BCS is an SBA-certified, HUBZone, EDWOSB business with more than 10 years of experience as environmental, natural resource, and cultural resource management specialists.</p>

  <h2 class="section-title">Corporate Overview</h2>
  <p>Founded in 2012, Cedar Ridge Environmental Services, LLC (CRES) is an Indian Small Business Economic Enterprise (ISBEE) and Small Disadvantaged Business (SDB) providing environmental consulting services and subject matter expertise including environmental planning and permitting compliance, environmental justice and tribal consultation, and environmental technical services to include environmental risk assessment and monitoring. The company is wholly owned by the Cedar Ridge Nation, a federally recognized tribe, with headquarters in Lakeview, Oklahoma.</p>

  <h2 class="section-title">About Cedar Ridge</h2>
  <p>The Cedar Ridge Nation is an oil, gas, and gaming tribe located within Cedar County, Oklahoma. One of the oldest federally recognized tribes, the Nation operates numerous departments and programs designed to protect and improve the quality of life of its 20,000+ tribal members.</p>

  <h2 class="section-title">Corporate Data</h2>
  <div class="data-grid">
    <span>DUNS: 078412690</span><span>Cedar Ridge Environmental Services, LLC</span>
    <span>CAGE: 7KR2B</span><span>210 E. Elm Street, Suite 400</span>
    <span>TIN: 46-1938205</span><span>Lakeview, OK 74000</span>
  </div>

  <h2 class="section-title">NAICS Codes – [ABBREVIATED LIST]</h2>
  <ul class="ring-list">
    <li>541620 – Environmental Consulting Services, size: standard</li>
    <li>541690 – Other Scientific and Technical Consulting Services, size standard</li>
    <li>541990 – All other Professional, Scientific, and Technical Services, size standard</li>
  </ul>

  <h2 class="section-title">Discriminators</h2>
  <ul class="ring-list">
    <li>A long-standing, trusted relationship with the federal government.</li>
    <li>A tradition in land management trailing back to the 1880s and spanning more than 1.4 million acres.</li>
    <li>A highly competitive, low-indirect cost structure.</li>
  </ul>
</section>

<footer class="footer">
  <h3>CONTACT INFORMATION</h3>
  <div class="line name">Kevin Walsh</div>
  <div class="line">Director, Strategic Programs and Partnerships</div>
  <div class="line">E: k.walsh@cedarridge-env.example &nbsp;|&nbsp; M: (918) 555-0142</div>
</footer>
</body>
</html>
```